Brenford Works Business Card

Modern and Professional Business Card for a Med size construction/development company.

See the samples below for the design I like … but I need ideas for incorporating the red company logo while still keeping the clean look of the card samples that are attached.

Logo and tag line on the back … info on the front.

Tagline: Quality Starts from the Ground Up

Target Market(s)

Med-Large General Contractors

Contact Information for Business Card

Brenford Works Limited
42 Marsh Lane
Mt. Pearl, NL
A1N 6T2

t: 709-555-0142
f: 709-555-0187
w: www.brenfordworks.example

Font styles to use
Sans Serif

Colors
fbee3e

Requirements
Must have
• I like the black and yellow designs of the attached samples …. but I'm not sure how to incorporate the red Brenford Works logo into that design??
Nice to have
• Construction safety strips

```html
<!DOCTYPE html>
<html lang="en">
<head>
<meta charset="utf-8">
<title>Brenford Works Business Card</title>
<link href="https://fonts.googleapis.com/css2?family=Montserrat:wght@400;500;700;800&family=Quicksand:wght@400;500;600&display=swap" rel="stylesheet">
<style>
  :root {
    --backdrop: #262624;
    --card-dark: #141414;
    --card-mid: #3a3a3a;
    --brand-red: #e3191f;
    --safety-yellow: #fbee3e;
    --text-light: #f2f2f2;
    --text-soft: #cfcfcf;
    --rule: #8a8a8a;
  }
  * { margin: 0; padding: 0; box-sizing: border-box; }
  html, body { width: 1200px; height: 960px; overflow: hidden; }
  body {
    background: var(--backdrop);
    font-family: "Quicksand", sans-serif;
    color: var(--text-light);
    position: relative;
  }
  .card {
    position: absolute;
    left: 300px;
    width: 600px;
    height: 343px;
    border-radius: 18px;
    overflow: hidden;
    background:
      repeating-linear-gradient(100deg, rgba(255,255,255,0.025) 0 1px, transparent 1px 4px),
      repeating-linear-gradient(10deg, rgba(0,0,0,0.12) 0 1px, transparent 1px 5px),
      radial-gradient(ellipse at 55% 40%, var(--card-mid) 0%, #222 50%, var(--card-dark) 100%);
    box-shadow: 0 18px 40px rgba(0,0,0,0.6);
  }
  .card-back { top: 100px; }
  .card-front { top: 497px; }

  /* back */
  .back-brand {
    position: absolute;
    left: 0; right: 0; top: 104px;
    display: flex; align-items: center; justify-content: center; gap: 14px;
  }
  .brand-mark {
    width: 22px; height: 22px;
    background: var(--brand-red);
  }
  .brand-name {
    font-family: "Montserrat", sans-serif;
    font-weight: 800;
    font-size: 32px;
    letter-spacing: 1px;
    color: var(--text-light);
    white-space: nowrap;
  }
  .tagline {
    position: absolute;
    left: 0; right: 0; top: 160px;
    text-align: center;
    font-size: 15px;
    font-weight: 600;
    letter-spacing: 2px;
    text-transform: uppercase;
    color: var(--safety-yellow);
  }
  .back-web {
    position: absolute;
    left: 0; right: 0; top: 222px;
    text-align: center;
    font-size: 15px;
    letter-spacing: 6px;
    color: var(--text-soft);
  }
  .back-web .accent { color: var(--brand-red); }

  /* front */
  .front-brand {
    position: absolute;
    left: 34px; top: 150px;
    display: flex; align-items: center; gap: 10px;
  }
  .front-brand .brand-name { font-size: 22px; }
  .front-brand .brand-mark { width: 16px; height: 16px; }
  .divider {
    position: absolute;
    left: 326px; top: 52px;
    width: 1px; height: 208px;
    background: var(--rule);
  }
  .contact {
    position: absolute;
    left: 350px; top: 48px;
  }
  .person-name {
    font-family: "Montserrat", sans-serif;
    font-weight: 500;
    font-size: 21px;
    letter-spacing: 0.5px;
  }
  .person-title {
    color: var(--brand-red);
    font-size: 14px;
    margin-bottom: 16px;
  }
  .address { font-size: 14px; line-height: 1.45; color: var(--text-soft); margin-bottom: 12px; }
  .lines { list-style: none; font-size: 14px; line-height: 1.55; color: var(--text-soft); }
  .lines li { display: flex; align-items: center; gap: 8px; }
  .lines svg { width: 12px; height: 12px; fill: var(--brand-red); flex: none; }
  .safety-strip {
    position: absolute;
    left: 0; right: 0; bottom: 0;
    height: 26px;
    background: repeating-linear-gradient(115deg, var(--brand-red) 0 9px, transparent 9px 22px);
  }
</style>
</head>
<body>
  <section class="card card-back">
    <div class="back-brand">
      <span class="brand-mark"></span>
      <span class="brand-name">BRENFORD WORKS LIMITED</span>
    </div>
    <p class="tagline">Quality Starts from the Ground Up</p>
    <p class="back-web"><span class="accent">www.</span>brenfordworks<span class="accent">.example</span></p>
  </section>

  <section class="card card-front">
    <div class="front-brand">
      <span class="brand-mark"></span>
      <span class="brand-name">BRENFORD WORKS</span>
    </div>
    <div class="divider"></div>
    <div class="contact">
      <p class="person-name">DANA WHITLOCK</p>
      <p class="person-title">President</p>
      <p class="address">Brenford Works Limited<br>42 Marsh Lane<br>Mt. Pearl, NL A1N 6T2</p>
      <ul class="lines">
        <li><svg viewBox="0 0 24 24"><path d="M6.6 10.8a15 15 0 0 0 6.6 6.6l2.2-2.2a1 1 0 0 1 1-.25 11.4 11.4 0 0 0 3.6.57 1 1 0 0 1 1 1V20a1 1 0 0 1-1 1A17 17 0 0 1 3 4a1 1 0 0 1 1-1h3.5a1 1 0 0 1 1 1c0 1.25.2 2.45.57 3.6a1 1 0 0 1-.25 1z"/></svg>709-555-0142</li>
        <li><svg viewBox="0 0 24 24"><path d="M6 3h10v5H6zM4 9h16a2 2 0 0 1 2 2v6h-4v4H6v-4H2v-6a2 2 0 0 1 2-2zm4 7v3h8v-3z"/></svg>709-555-0187</li>
        <li><svg viewBox="0 0 24 24"><circle cx="12" cy="12" r="10"/></svg>www.brenfordworks.example</li>
      </ul>
    </div>
    <div class="safety-strip"></div>
  </section>
</body>
</html>
```